Contemporary new French wine brand needs logo and series of label design

to design a new contemporary logo and series of labels for a new French wine brand. We hope to attract not just current French wine drinkers but new ones who may appreciate a less traditional and more modern style.
Updates

Reason: we are wanting to extend the project for a few days more to receive more submissions since we had fewer designs submitted than we were expecting, maybe because of the holidays.

Target Market(s)

people who follow the arts community (eg. music, theatre, visual/video arts, dance) --- all mature ages.

Industry/Entity Type

French Wine

Requirements
Must have
• a clear, memorable treatment for the name CLAVINE with accompanying logo.
Nice to have
• embossing, matte/gloss refinement, tasteful foil stamping, coated stock for the whites to help the integrity of the paper in and out of ice buckets. A combo of say, three types of fonts; a semi custom font for the brand name Clavine and maybe a script and one other.
Should not have
• not traditional French

```html
<!DOCTYPE html>
<html lang="en">
<head>
<meta charset="UTF-8">
<title>Clavine – Sauvignon Blanc Label</title>
<link rel="stylesheet" href="https://fonts.googleapis.com/css2?family=Cinzel+Decorative:wght@700&display=swap">
<style>
  :root {
    --ink: #0a0b0c;
    --gold: #e9b823;
    --gold-light: #f7e6a0;
    --gold-deep: #b98a10;
    --white: #ffffff;
  }
  * { margin: 0; padding: 0; box-sizing: border-box; }
  html, body {
    width: 1200px;
    height: 1200px;
    overflow: hidden;
    background: var(--ink);
  }
  .label {
    position: relative;
    width: 1200px;
    height: 1200px;
    background: var(--ink);
  }
  .label__frame {
    position: absolute;
    left: 43px;
    top: 43px;
    width: 1114px;
    height: 1114px;
    border: 8px solid var(--gold);
  }
  .label__brand {
    position: absolute;
    left: 0;
    right: 0;
    top: 200px;
    text-align: center;
    font-family: "Cinzel Decorative", serif;
    font-weight: 700;
    font-size: 150px;
    line-height: 1;
    color: var(--gold);
  }
  .label__variety {
    position: absolute;
    left: 0;
    right: 0;
    top: 462px;
    text-align: center;
    font-family: "Cinzel Decorative", serif;
    font-weight: 700;
    font-size: 60px;
    letter-spacing: 1px;
    line-height: 1;
    color: var(--white);
  }
  .label__landscape {
    position: absolute;
    left: 58px;
    top: 607px;
    width: 1088px;
    height: 433px;
    background:
      linear-gradient(180deg,
        rgba(233,184,35,0) 0%,
        rgba(247,230,160,0.55) 30%,
        var(--gold) 60%,
        rgba(185,138,16,0.45) 61%,
        rgba(185,138,16,0.12) 85%,
        rgba(10,11,12,0) 100%);
  }
</style>
</head>
<body>
  <main class="label">
    <div class="label__frame"></div>
    <h1 class="label__brand">Clavine</h1>
    <p class="label__variety">Sauvignon Blanc</p>
    <div class="label__landscape" role="img" aria-label="Gold mountain range above a horizon line, mirrored as a fading reflection in still water"></div>
  </main>
</body>
</html>
```